Political Candidate Newspaper Advertisement

I would like a newspaper ad for my campaign for election to City Council. The banner ad is 10 cm high x 26.2 cm wide. The banner will contain a photo and the following text (or words to similar effect):
VOTE
DENNIS HALE
COMO BEACH
For a
SAFE
CARING
CONNECTED
COMMUNITY
Lifetime commitment to local clubs, charities and international aid
Local business owner
Founder of Open-Gate Week
Councillor, Mediator, B.Sc., MBA
The Councillor you know and can call for help
Respects our heritage and our future
Listens to the wisdom and needs of older residents
Promotes more young people
Protects our South Perth environment
Authorised by Dennis Hale 5/348 Kelby Rd, Como. 9317 2864
I use MS Publisher and PhotoShop so I'd like the product to be in a form I can use. After ther banner ad is done, and if it is good, I wish to pay the designer to use the same theme to produce another newspaper ad, a brochure and a poster.
My simple version is attached. A photo is also attached.
I'm hoping you do better.
18-80 years old
Business
- simple fonts
- A TICK somewhere around the word Vote would be good.
Mention of www.fairlandward.notepage.net if possible, perhaps at the bottom of the page, along with the Authorised by ... text.

```html
<!DOCTYPE html>
<html lang="en">
<head>
<meta charset="utf-8">
<title>Vote Dennis Hale – Como Beach</title>
<link rel="stylesheet" href="https://fonts.googleapis.com/css2?family=Archivo+Black&family=Cinzel:wght@700&family=Lato:wght@700;900&family=Oswald:wght@600&display=swap">
<style>
  :root {
    --mat: #d9dadc;
    --paper: #ffffff;
    --vote-red: #e0101f;
    --band-red: #d0102a;
    --band-red-dark: #b00d22;
    --navy: #1f2f8f;
    --ink: #1a1a1a;
    --band-text: #ffffff;
    --fine-print: #6e0a16;
    --photo-blue: #2a3d8c;
    --photo-red: #b8313d;
    --photo-dark: #2b2b2b;
  }
  * { margin: 0; padding: 0; box-sizing: border-box; }
  html, body { width: 1200px; height: 510px; overflow: hidden; background: var(--mat); }
  .canvas { position: relative; width: 1200px; height: 510px; }
  .ad {
    position: absolute; left: 43px; top: 42px; width: 1114px; height: 424px;
    background: var(--paper); overflow: hidden;
  }
  .candidate-photo {
    position: absolute; left: 0; top: 0; width: 445px; height: 424px;
    background:
      linear-gradient(90deg, rgba(255,255,255,0) 55%, var(--paper) 100%),
      linear-gradient(180deg, rgba(0,0,0,0) 45%, var(--photo-dark) 100%),
      linear-gradient(135deg, var(--photo-red) 0%, var(--photo-blue) 30%, var(--photo-blue) 60%, #c9d0e6 100%);
  }
  .tick { position: absolute; left: 311px; top: 20px; width: 120px; height: 119px; }
  .vote {
    position: absolute; left: 443px; top: 40px;
    font: 400 63px/1 "Archivo Black", sans-serif; color: var(--vote-red);
  }
  .name {
    position: absolute; left: 343px; top: 104px; width: 298px; height: 160px; text-align: center;
    font-family: "Cinzel", serif; font-weight: 700; color: var(--navy); line-height: 1;
  }
  .name-first { display: block; font-size: 60px; letter-spacing: -1px; }
  .name-last {
    display: block; font-size: 104px; letter-spacing: -2px;
    transform: scaleY(1.22); transform-origin: center top; margin-top: -4px;
  }
  .ward {
    position: absolute; left: 350px; top: 270px; width: 290px; text-align: center;
    font: 900 39px/1 "Lato", sans-serif; color: var(--ink); letter-spacing: 0.5px;
  }
  .credentials {
    position: absolute; top: 42px; list-style: none;
    font: 700 17px/21px "Lato", sans-serif; color: var(--ink);
  }
  .credentials-left { left: 677px; width: 214px; }
  .credentials-right { left: 909px; width: 190px; }
  .credentials li { position: relative; padding-left: 13px; margin-bottom: 11px; }
  .credentials li::before { content: "•"; position: absolute; left: 0; }
  .slogan-band {
    position: absolute; left: 326px; top: 329px; width: 788px; height: 95px;
    background: linear-gradient(90deg, var(--band-red) 0%, var(--band-red-dark) 100%);
  }
  .slogan {
    position: absolute; left: 30px; top: 6px; white-space: nowrap;
    font: 600 46px/1.2 "Oswald", sans-serif; color: var(--band-text); letter-spacing: -0.5px;
    transform: scaleX(0.82); transform-origin: left center;
  }
  .authorisation {
    position: absolute; right: 21px; bottom: 10px; white-space: nowrap;
    font: 400 13px/1 Arial, sans-serif; color: var(--fine-print);
  }
</style>
</head>
<body>
<div class="canvas">
  <section class="ad">
    <div class="candidate-photo" role="img" aria-label="Portrait of the candidate in suit and tie in front of a waving Australian flag"></div>

    <svg class="tick" viewBox="0 0 122 120" aria-hidden="true">
      <path d="M0 62 C14 58 26 64 40 86 C60 44 88 16 122 0 C92 26 66 62 46 120 C32 96 20 76 0 62 Z" fill="var(--vote-red)"/>
    </svg>

    <div class="vote">VOTE</div>
    <h1 class="name">
      <span class="name-first">DENNIS</span>
      <span class="name-last">HALE</span>
    </h1>
    <div class="ward">COMO BEACH</div>

    <ul class="credentials credentials-left">
      <li>Lifetime commitment to local clubs, charities and international aid</li>
      <li>Local business owner</li>
      <li>Founder of Open-Gate Week</li>
      <li>Councillor, Mediator, B.Sc., MBA</li>
      <li>The Councillor you know and can call for help</li>
    </ul>
    <ul class="credentials credentials-right">
      <li>Respects our heritage and our future</li>
      <li>Listens to the wisdom and needs of older residents</li>
      <li>Promotes more young people</li>
      <li>Protects our South Perth environment</li>
    </ul>

    <div class="slogan-band">
      <p class="slogan">For a SAFE • CARING • CONNECTED • COMMUNITY</p>
      <p class="authorisation">Authorised by Dennis Hale 5/348 Kelby Rd, Como. 9317 2864. www.fairlandward.notepage.net</p>
    </div>
  </section>
</div>
</body>
</html>
```